New Bicycle shop business card

Hi!
I'm looking for a business card for my new proffesional bike mechanics shop. This shop is only for fixing broken bikes and not selling bikes.
Peferbly a modern and sleek and modern design.
Colors: black, grey, red, white
Information:
Name: Velowerkplaats Martens
Shop owner: Bart Martens & Sofie Vanhulle
Website: www.velowerkplaats-martens.be
Email: info@velowerkplaats-martens.be
Phone number: +32471936208
Street adres: Molenweg 57
9470 Oostmeerbeke
Slogan/shop information: Herstellingen van alle merken.
Logo: see files.
Target Market(s)
People who seek a mechanic to fix or upgrade their bikes.
Contact Information for Business Card
Information:
Website: info@velowerkplaats-martens.be
9470 Oostmeerbeke
Logo: see files.

```html
<!DOCTYPE html>
<html lang="nl">
<head>
<meta charset="utf-8">
<title>Velowerkplaats Martens – Business Card</title>
<link rel="stylesheet" href="https://fonts.googleapis.com/css2?family=Lato:wght@400;700;900&family=EB+Garamond:ital@1&display=swap">
<style>
  :root {
    --backdrop: #e8e6e4;
    --card-black: #1c1716;
    --brand-red: #e3173e;
    --text-white: #ffffff;
  }
  * { margin: 0; padding: 0; box-sizing: border-box; }
  html, body {
    width: 1200px;
    height: 900px;
    overflow: hidden;
    background: var(--backdrop);
  }
  .business-card {
    position: absolute;
    left: 100px;
    top: 141px;
    width: 1000px;
    height: 618px;
    background: var(--card-black);
    overflow: hidden;
    font-family: "Lato", Arial, sans-serif;
    color: var(--text-white);
    box-shadow: 0 10px 30px rgba(0,0,0,0.18);
  }
  .card-accent {
    position: absolute;
    inset: 0;
    width: 1000px;
    height: 618px;
  }
  .contact-block {
    position: absolute;
    left: 38px;
    top: 76px;
  }
  .owner-names {
    font-weight: 700;
    font-size: 34px;
    line-height: 44px;
    color: var(--brand-red);
    letter-spacing: 0.3px;
  }
  .owner-role {
    font-size: 26px;
    line-height: 34px;
    margin-top: 2px;
  }
  .address {
    font-style: normal;
    font-size: 27px;
    line-height: 37px;
    margin-top: 30px;
  }
  .contact-list {
    list-style: none;
    margin-top: 22px;
  }
  .contact-item {
    display: flex;
    align-items: center;
    font-size: 26px;
    line-height: 37px;
  }
  .contact-icon {
    width: 18px;
    height: 18px;
    margin-right: 12px;
    flex: none;
  }
  .slogan {
    position: absolute;
    left: 42px;
    top: 506px;
    font-family: "EB Garamond", Georgia, serif;
    font-style: italic;
    font-size: 36px;
    color: var(--brand-red);
  }
  .shop-name {
    position: absolute;
    left: 473px;
    top: 220px;
    width: 440px;
    text-align: center;
  }
  .shop-name-dot {
    display: block;
    width: 48px;
    height: 48px;
    margin: 0 auto 26px;
    border-radius: 50%;
    background: var(--brand-red);
  }
  .shop-name-text {
    font-weight: 900;
    font-size: 34px;
    line-height: 44px;
    letter-spacing: 2px;
    color: var(--text-white);
  }
</style>
</head>
<body>
  <section class="business-card">
    <svg class="card-accent" viewBox="0 0 1000 618" aria-hidden="true">
      <path d="M 735 0 H 1000 V 618 H 690 C 860 500 930 250 870 40 C 860 20 800 5 735 0 Z" fill="var(--brand-red)"/>
    </svg>

    <div class="contact-block">
      <h1 class="owner-names">BART MARTENS &amp;<br>SOFIE VANHULLE</h1>
      <p class="owner-role">Owner</p>
      <address class="address">Molenweg 57<br>9470 Oostmeerbeke</address>
      <ul class="contact-list">
        <li class="contact-item">
          <svg class="contact-icon" viewBox="0 0 20 20"><path fill="var(--brand-red)" d="M2 7c0-2 3-4 8-4s8 2 8 4v2h-4V7.5c-1-.6-2.4-.9-4-.9s-3 .3-4 .9V9H2zM5 10h10l2 7H3z"/><circle cx="10" cy="13.5" r="2" fill="var(--card-black)"/></svg>
          +32471936208
        </li>
        <li class="contact-item">
          <svg class="contact-icon" viewBox="0 0 20 20"><rect x="1" y="4" width="18" height="13" fill="var(--brand-red)"/><path d="M1.5 4.5 10 11l8.5-6.5" fill="none" stroke="var(--card-black)" stroke-width="1.6"/></svg>
          info@velowerkplaats-martens.be
        </li>
        <li class="contact-item">
          <svg class="contact-icon" viewBox="0 0 20 20"><circle cx="10" cy="10" r="9" fill="var(--brand-red)"/><path d="M6 5c2 1 1 3 3 3s1 3 3 3-1 3 1 4M13 4c-1 1 0 2 2 2" fill="none" stroke="var(--card-black)" stroke-width="1.5"/></svg>
          www.velowerkplaats-martens.be
        </li>
      </ul>
    </div>

    <p class="slogan">Herstellingen van alle merken</p>

    <div class="shop-name">
      <span class="shop-name-dot"></span>
      <p class="shop-name-text">VELOWERKPLAATS<br>MARTENS</p>
    </div>
  </section>
</body>
</html>
```